New Business Card Design for Manufacturing

We are an engineering/manufacturing company that offers Advanced machining/assembly/engineering services, as well as innovative products for the heavy duty engine cooling markets.

We are looking to get a new business card designed that is clean and modern looking, but still fits the wide range of technical/skilled work we do.

- We hope to use this design as the base for other design work in new Presentations, web, and print work.

Industry/Entity Type

Engineering

Contact Information for Business Card

Our preferred color of blue is (RGB) 22/71/159 but can vary slightly from that color. Our content will be our Logo and full company name (Fabricated Tooling Works, Inc.), company address, name, job title, phone number with extension, cell number, fax number, website, and email address on the cards.
We'd like the full company name next to the logo, but we are open to other interpretations of that layout.
Preferably, we would like the back side to be clean with just our logo, and the front to contain all of the contact information.

Colors
2f74b4
0355a3
85abd2

Requirements
Must have
• - Logo, company name, needed content - We are open to interpretation beyond that.
• - Standard size business card.
• - Horizontal orientation.
• - Enough space for lengthy names / job titles (for example, a job title could read "Directory of Human Resources" or "V.P. of Governmental Affairs"). We need this to look clean, whether the title be short (CEO) or long (as described above).

```html
<!DOCTYPE html>
<html lang="en">
<head>
<meta charset="utf-8">
<title>Fabricated Tooling Works – Business Card</title>
<link rel="stylesheet" href="https://fonts.googleapis.com/css2?family=Open+Sans:wght@400;600&display=swap">
<style>
  :root {
    --brand-blue: #0f55a3;
    --accent-blue: #4db3e6;
    --pale-blue: #a9d2f2;
    --ink: #444448;
    --muted: #5a5a60;
    --card: #ffffff;
    --backdrop: #e4e4e6;
  }
  * { box-sizing: border-box; margin: 0; padding: 0; }
  html, body { width: 1200px; height: 1000px; overflow: hidden; }
  body {
    background: var(--backdrop);
    font-family: "Open Sans", Arial, sans-serif;
    position: relative;
  }
  .card {
    position: absolute;
    left: 220px;
    width: 760px;
    height: 434px;
    background: var(--card);
    overflow: hidden;
    box-shadow: 0 6px 18px rgba(0,0,0,0.18);
  }
  .card--front { top: 50px; }
  .card--back { top: 516px; }
  .card__shapes { position: absolute; inset: 0; width: 760px; height: 434px; }

  /* Front */
  .company-name {
    position: absolute; left: 40px; top: 70px; width: 210px;
    color: var(--brand-blue);
    font-weight: 600; font-size: 17px; line-height: 1.3;
  }
  .person { position: absolute; left: 300px; width: 360px; top: 72px; text-align: center; }
  .person__name { font-size: 27px; letter-spacing: 2px; color: var(--ink); font-weight: 400; }
  .person__title { font-size: 13.5px; letter-spacing: 1.2px; color: var(--muted); margin-top: 6px; text-transform: uppercase; }
  .address {
    position: absolute; left: 300px; width: 360px; top: 174px;
    display: flex; align-items: center; justify-content: center; gap: 10px;
    color: #fff; font-size: 14px; letter-spacing: 1px; text-transform: uppercase;
  }
  .contact-list { position: absolute; list-style: none; }
  .contact-list--left { left: 62px; top: 296px; }
  .contact-list--right { left: 480px; top: 236px; }
  .contact-list li {
    display: flex; align-items: center; gap: 12px;
    font-size: 14px; letter-spacing: 1.2px; color: var(--muted);
    text-transform: uppercase; height: 28px;
  }
  .icon { width: 16px; height: 16px; fill: var(--ink); flex: none; }

  /* Back */
  .brand {
    position: absolute; left: 0; right: 0; top: 192px; text-align: center;
    color: var(--brand-blue); font-weight: 600; font-size: 44px; line-height: 1.2;
  }
  .web {
    position: absolute; left: 360px; width: 320px; top: 372px;
    text-align: center; color: #fff; font-size: 19px;
  }
</style>
</head>
<body>

<section class="card card--front" aria-label="Business card front">
  <svg class="card__shapes" viewBox="0 0 760 434" aria-hidden="true">
    <path d="M0 0 H760 V62 C758 32 745 20 715 20 L70 20 C35 20 12 30 0 50 Z" fill="var(--brand-blue)"/>
    <path d="M240 185 H722 V206 C722 222 712 230 696 230 L266 230 C250 230 240 222 240 206 Z" fill="var(--pale-blue)"/>
    <path d="M280 165 H682 C692 165 698 172 698 182 V196 C698 206 690 214 680 214 L282 214 C272 214 264 206 264 196 V182 C264 172 270 165 280 165 Z" fill="var(--accent-blue)"/>
    <line x1="0" y1="185" x2="760" y2="185" stroke="var(--accent-blue)" stroke-width="2"/>
  </svg>

  <div class="company-name">Fabricated Tooling Works, Inc.</div>

  <div class="person">
    <div class="person__name">NAME OF CEO</div>
    <div class="person__title">Directory of Human Resources</div>
  </div>

  <div class="address">
    <svg class="icon" viewBox="0 0 16 16" style="fill:#fff"><path d="M8 1a5 5 0 0 0-5 5c0 3.8 5 9 5 9s5-5.2 5-9a5 5 0 0 0-5-5zm0 7a2 2 0 1 1 0-4 2 2 0 0 1 0 4z"/></svg>
    <span>Your company address</span>
  </div>

  <ul class="contact-list contact-list--right">
    <li><svg class="icon" viewBox="0 0 16 16"><circle cx="8" cy="8" r="6.5" fill="none" stroke="var(--ink)" stroke-width="1.5"/><ellipse cx="8" cy="8" rx="2.6" ry="6.5" fill="none" stroke="var(--ink)" stroke-width="1.2"/><line x1="1.5" y1="8" x2="14.5" y2="8" stroke="var(--ink)" stroke-width="1.2"/></svg>Website</li>
    <li><svg class="icon" viewBox="0 0 16 16"><path d="M1 3.5h14v9H1z"/><path d="M1 3.5l7 5 7-5" fill="none" stroke="#fff" stroke-width="1.2"/></svg>Email address</li>
  </ul>

  <ul class="contact-list contact-list--left">
    <li><svg class="icon" viewBox="0 0 16 16"><path d="M2 5c0-2 2-3 6-3s6 1 6 3v1h-3V5H5v1H2z"/><path d="M4 8l1.5-2h5L12 8v6H4z"/><circle cx="8" cy="10.5" r="1.6" fill="#fff"/></svg>Phone number</li>
    <li><svg class="icon" viewBox="0 0 16 16"><path d="M4 1.5l2.3 3-1.4 1.6c.8 2 2.4 3.6 4.4 4.5l1.6-1.5 3 2.3-1.2 2.6C7.5 14 2 8.5 1.5 3.3z"/></svg>Cell number</li>
    <li><svg class="icon" viewBox="0 0 16 16"><path d="M4 1h8v4H4z"/><path d="M1 6h14v6h-3v3H4v-3H1z"/><path d="M5.5 10h5v3.5h-5z" fill="#fff"/></svg>Fax number</li>
  </ul>
</section>

<section class="card card--back" aria-label="Business card back">
  <svg class="card__shapes" viewBox="0 0 760 434" aria-hidden="true">
    <path d="M105 0 H650 C650 48 628 100 575 100 L200 100 C150 100 128 70 105 0 Z" fill="var(--brand-blue)"/>
    <path d="M330 434 C340 375 362 352 405 352 L640 352 C672 352 690 370 705 434 Z" fill="var(--brand-blue)"/>
    <line x1="40" y1="300" x2="170" y2="292" stroke="var(--accent-blue)" stroke-width="2"/>
    <line x1="600" y1="170" x2="735" y2="160" stroke="var(--accent-blue)" stroke-width="2"/>
  </svg>

  <div class="brand">Fabricated Tooling Works</div>

  <div class="web">www.website.com</div>
</section>

</body>
</html>
```